We need a simple unsiversal design for all our products. Please work with our template (sample) and the attached logo. The color shoulderstand match with the logo.

Industry/Entity Type

Nutrition

```html
<!DOCTYPE html>
<html lang="en">
<head>
<meta charset="utf-8">
<title>Produkt – Product Label</title>
<link rel="stylesheet" href="https://fonts.googleapis.com/css2?family=Lato:wght@400;700;900&family=Lobster&family=Oswald:wght@500&display=swap">
<style>
  :root {
    --stage: #ecebe8;
    --blue-deep: #0b74c4;
    --blue-mid: #1d93d9;
    --blue-light: #5cc3ec;
    --blue-pale: #c4ecfa;
    --frame: #3ed2f0;
    --ink: #141a2b;
    --paper: #ffffff;
    --wave-shade: #c3d3dc;
    --wave-line: #8fb3c6;
  }
  * { margin: 0; padding: 0; box-sizing: border-box; }
  html, body { width: 1200px; height: 714px; overflow: hidden; background: var(--stage); }
  body { position: relative; font-family: "Lato", sans-serif; color: var(--ink); }

  .label {
    position: absolute; left: 26px; top: 120px; width: 1148px; height: 474px; overflow: hidden;
    background:
      radial-gradient(ellipse 30% 70% at 50% 40%, rgba(8,100,180,.85) 0%, rgba(8,100,180,0) 100%),
      linear-gradient(90deg, var(--blue-light) 0%, var(--blue-mid) 28%, var(--blue-deep) 50%, var(--blue-mid) 72%, var(--blue-pale) 100%);
    box-shadow: 0 6px 18px rgba(0,0,0,.25);
  }
  .label__texture {
    position: absolute; inset: 0;
    background:
      radial-gradient(ellipse 40% 45% at 8% 70%, rgba(255,255,255,.55), transparent 70%),
      radial-gradient(ellipse 35% 45% at 95% 60%, rgba(255,255,255,.45), transparent 70%),
      linear-gradient(180deg, rgba(255,255,255,0) 0%, rgba(255,255,255,0) 28%, rgba(255,255,255,.12) 30%, rgba(255,255,255,.12) 100%);
  }
  .frame { position: absolute; top: 140px; height: 250px; border: 2px solid var(--frame); }
  .frame--left { left: -2px; width: 443px; }
  .frame--right { left: 712px; width: 440px; }

  .text { position: absolute; font-size: 14.5px; line-height: 18.4px; white-space: nowrap; }
  .text b { font-weight: 700; }
  .text--intro-left { left: 23px; top: 22px; }
  .text--intro-right { right: 12px; top: 22px; text-align: right; }
  .text--note-left { left: 34px; top: 324px; }

  .title {
    position: absolute; left: 0; width: 1148px; top: 18px; text-align: center;
    font-family: "Lobster", cursive; font-size: 80px; line-height: 96px; color: var(--paper);
    text-shadow: 0 3px 6px rgba(0,0,0,.35);
  }
  .subline {
    position: absolute; left: 0; width: 1148px; top: 107px; text-align: center;
    font-family: "Oswald", sans-serif; font-weight: 500; font-size: 22px; line-height: 30px; color: var(--ink);
  }
  .product-icon {
    position: absolute; left: 534px; top: 170px; width: 78px; height: 94px; border-radius: 39px;
    background: linear-gradient(160deg, rgba(40,110,170,.5), rgba(10,60,110,.65));
  }

  .nutrition-table { position: absolute; left: 0; top: 0; font-weight: 700; }
  .nutrition-table__caption { position: absolute; left: 19px; top: 136px; font-size: 14.5px; color: var(--paper); white-space: nowrap; }
  .nutrition-table__head, .nutrition-table__cell { position: absolute; font-size: 15px; line-height: 19px; white-space: nowrap; }
  .nutrition-table__cell { line-height: 17px; }

  .brand { position: absolute; left: 502px; top: 346px; width: 144px; display: flex; align-items: center; justify-content: center; gap: 8px; }
  .brand__dot { width: 14px; height: 14px; border-radius: 50%; background: var(--ink); flex: none; }
  .brand__name { font-size: 27px; font-weight: 700; color: var(--ink); line-height: 1; }

  .text--info-heading { right: 14px; top: 154px; font-size: 16px; line-height: 20px; font-weight: 700; text-align: right; }
  .text--info-body { right: 14px; top: 177px; font-size: 16.4px; line-height: 20.2px; font-weight: 700; text-align: right; }
  .text--info-foot { right: 8px; top: 335px; font-size: 16px; line-height: 20.2px; text-align: right; }

  .wave { position: absolute; left: 0; top: 0; width: 1148px; height: 474px; }
</style>
</head>
<body>
  <main class="label">
    <div class="label__texture" role="img" aria-label="Soft blue medical background with faint crosses"></div>

    <svg class="wave" viewBox="0 0 1148 474" aria-hidden="true">
      <path d="M0,402 C260,396 460,456 740,456 C920,456 1060,430 1148,382 L1148,474 L0,474 Z" fill="var(--wave-shade)"/>
      <path d="M0,414 C270,406 470,468 750,466 C930,464 1065,440 1148,396 L1148,474 L0,474 Z" fill="var(--paper)"/>
      <path d="M0,396 C290,386 490,448 780,446" fill="none" stroke="var(--wave-line)" stroke-width="1.5" opacity=".6"/>
    </svg>

    <div class="frame frame--left"></div>
    <div class="frame frame--right"></div>

    <p class="text text--intro-left"><b>Lorem ipsum dolor:</b> sit amet, consectetur<br>adipiscing elit. Aliquam ac viverra lorem.<br>Aliquam eget euismod justo, vel efficitur mi.<br>Vestibulum ac diam quis eratlobortis massa<br>odio, vitae molestie erat commod.</p>
    <p class="text text--intro-right">Lorem ipsum dolor sit amet, consectetur<br>adipiscing elit. Aliquam ac viverra lorem.<br>Aliquam eget euismod justo, vel efficitur mi.<br>Vestibulum ac diam quis eratlobortis massa<br>odio, vitae molestie erat commod.</p>

    <h1 class="title">Produkt</h1>
    <p class="subline">Sub-Line Goes here</p>
    <div class="product-icon" role="img" aria-label="Capsule and tablet icon"></div>

    <section class="nutrition-table">
      <p class="nutrition-table__caption">Lorem ipsum dolor= Dffus 5 lps:</p>
      <span class="nutrition-table__head" style="left:38px;top:163px;text-align:center">Lorem ipsum<br>(Lorem ipsum)</span>
      <span class="nutrition-table__head" style="left:158px;top:166px">Lorem<br>Lorem</span>
      <span class="nutrition-table__head" style="left:238px;top:166px;text-align:center">Lorem ipsum<br>(Lorem ipsum)</span>
      <span class="nutrition-table__head" style="left:341px;top:166px;text-align:center">Lore<br>Lorem</span>
      <span class="nutrition-table__cell" style="left:46px;top:218px">AAA<br>AAA</span>
      <span class="nutrition-table__cell" style="left:139px;top:218px">00000<br>00000</span>
      <span class="nutrition-table__cell" style="left:222px;top:218px">000<br>000</span>
      <span class="nutrition-table__cell" style="left:331px;top:218px">000 XY<br>000 XY</span>
      <span class="nutrition-table__cell" style="left:46px;top:255px">AAA<br>AAA</span>
      <span class="nutrition-table__cell" style="left:139px;top:255px">00000<br>00000</span>
      <span class="nutrition-table__cell" style="left:222px;top:255px">000<br>000</span>
      <span class="nutrition-table__cell" style="left:331px;top:255px">000 XY<br>000 XY</span>
    </section>

    <p class="text text--note-left"><b>Lorem ipsum dolor:</b> sit amet, consectetur<br>adipiscing elit. Aliquam ac vi.</p>

    <div class="brand">
      <span class="brand__dot" aria-hidden="true"></span>
      <span class="brand__name">Veloria</span>
    </div>

    <p class="text text--info-heading">Lorem ipsum:</p>
    <p class="text text--info-body">Lorem ipsum dolor sit amet,<br>consectetur adipiscing elit. Ali-<br>quam ac viverra lorem. Aliquam<br>eget euismod justo, vel efficitur<br>mi. Vestibulum ac diam quis<br>eratlobortis massa odio, vitae<br>molestie erat commod.</p>
    <p class="text text--info-foot">Lorem ipsum dolor sit amet, consectetur adip-<br>iscing elit. Aliquam ac viverra lorem.</p>
  </main>
</body>
</html>
```